Larkfield Interiors
Stationary, Letterhead & Business Card
Larkfield Interiors -
Creative Brief
Professional
Dennis Coyle
Project Manager
478 Oakmont Avenue N.W. Millbrook, WI 53021
dennis@larkfield-interiors-studio.com
The information is fake, once the winning design is selected I will forward the correct contact information to the designer.

```html
<!DOCTYPE html>
<html lang="en">
<head>
<meta charset="utf-8">
<title>Larkfield Interiors – Stationery</title>
<link href="https://fonts.googleapis.com/css2?family=Arimo:wght@400;700&display=swap" rel="stylesheet">
<style>
  :root {
    --orange: #f08c1a;
    --amber: #f7b21f;
    --yellow: #fbd23a;
    --grey: #6d6e71;
    --ink: #3a3a3c;
    --paper: #ffffff;
    --stage: #ffffff;
  }
  * { box-sizing: border-box; margin: 0; padding: 0; }
  html, body { width: 1200px; height: 857px; overflow: hidden; background: var(--stage); }
  body { position: relative; font-family: "Arimo", Arial, sans-serif; color: var(--ink); }

  .brand { display: flex; align-items: center; gap: 8px; }
  .brand-mark { width: 22px; height: 22px; background: var(--orange); flex: none; }
  .brand-name { color: var(--grey); font-weight: 700; line-height: 1.02; letter-spacing: .06em; text-transform: uppercase; white-space: nowrap; }

  .letterhead {
    position: absolute; left: 36px; top: 12px; width: 564px; height: 833px;
    background: var(--paper); box-shadow: 0 1px 6px rgba(0,0,0,.25); overflow: hidden;
  }
  .letterhead .brand { position: absolute; right: 34px; top: 36px; }
  .letterhead .brand-name { font-size: 22px; }
  .letterhead .address { position: absolute; right: 34px; top: 94px; font-size: 10.5px; font-weight: 700; white-space: nowrap; }

  .letter-body { position: absolute; left: 60px; top: 160px; width: 470px; font-size: 9.6px; line-height: 13.6px; text-align: justify; color: #444; }
  .letter-body p { text-indent: 40px; margin-bottom: 14px; }

  .letter-footer { position: absolute; left: 0; bottom: 0; width: 564px; height: 70px;
    background: linear-gradient(to bottom, var(--yellow) 0 8px, var(--orange) 8px 52px, var(--amber) 52px 100%); }
  .letter-footer .contact { position: absolute; left: 0; right: 0; top: 24px; text-align: center; font-size: 10.5px; font-weight: 700; color: #fff; letter-spacing: .04em; white-space: nowrap; }

  .card {
    position: absolute; width: 540px; height: 263px; background: var(--paper);
    box-shadow: 0 1px 6px rgba(0,0,0,.25); overflow: hidden;
  }
  .card-front { left: 636px; top: 217px; }
  .card-back { left: 636px; top: 491px; }
  .person .name { font-size: 14px; font-weight: 700; color: var(--ink); }
  .person .role { font-size: 11px; color: var(--ink); margin-top: 2px; }

  .card-front .person { position: absolute; left: 26px; top: 24px; }
  .card-front .brand { position: absolute; left: 200px; top: 92px; }
  .card-front .brand-name { font-size: 22px; }
  .card-front .band { position: absolute; left: 0; right: 0; top: 150px; bottom: 0;
    background: linear-gradient(to bottom, var(--yellow) 0 6px, var(--orange) 6px 56px, var(--yellow) 56px 100%); }
  .card-front .contact { position: absolute; left: 26px; top: 176px; font-size: 9.5px; font-weight: 700; color: #fff; white-space: nowrap; }

  .card-back .side { position: absolute; left: 0; top: 40px; width: 22px; height: 160px;
    background: linear-gradient(to right, var(--orange) 0 14px, var(--yellow) 14px 100%); }
  .card-back .person { position: absolute; left: 250px; top: 36px; }
  .card-back .brand { position: absolute; left: 300px; top: 112px; }
  .card-back .brand-name { font-size: 20px; }
  .card-back .address { position: absolute; left: 300px; top: 168px; font-size: 9.5px; font-weight: 700; white-space: nowrap; }
  .card-back .contact { position: absolute; left: 26px; top: 220px; font-size: 9.5px; font-weight: 700; color: var(--ink); white-space: nowrap; }
  .card-back .base { position: absolute; left: 0; right: 0; bottom: 0; height: 14px; background: var(--amber); }
</style>
</head>
<body>

<section class="letterhead">
  <div class="brand">
    <span class="brand-mark"></span>
    <span class="brand-name">Larkfield<br>Interiors</span>
  </div>
  <div class="address">478 Oakmont Avenue N.W. Millbrook, WI 53021</div>

  <div class="letter-body">
    <p>I am submitting my resume to you in response to your advertisement for a Graphic Designer. I believe I have the skills that you are seeking and would like to be considered for this position. I have extensive layout and design experience and enjoy working on precise, detailed projects. I am highly organized and adept at meeting tight deadlines. I look forward to discussing this further with you. I am submitting my resume to you in response to your advertisement for a Graphic Designer. I believe I have the skills that you are seeking and would like to be considered for this position. I have extensive layout and design experience and enjoy working on precise, detailed projects. I am highly organized and adept at meeting tight deadlines. I look forward to discussing this further with you. I am submitting my resume to you in response to your advertisement for a Graphic Designer. I believe I have the skills that you are seeking and would like to be considered for this position. I have extensive layout and design experience and enjoy working on precise, detailed projects. I am highly organized and adept at meeting tight deadlines. I look forward to discussing this further with you. I am submitting my resume to you in response to your advertisement for a Graphic Designer. I believe I have the skills that you are seeking and would like to be considered for this position. I have extensive layout and design experience and enjoy working on precise, detailed projects. I am highly organized and adept at meeting tight deadlines. I look forward to discussing this further with you.</p>
    <p>I am submitting my resume to you in response to your advertisement for a Graphic Designer. I believe I have the skills that you are seeking and would like to be considered for this position. I have extensive layout and design experience and enjoy working on precise, detailed projects. I am highly organized and adept at meeting tight deadlines. I look forward to discussing this further with you. I am submitting my resume to you in response to your advertisement for a Graphic Designer. I believe I have the skills that you are seeking and would like to be considered for this position. I have extensive layout and design experience and enjoy working on precise, detailed projects. I am highly organized and adept at meeting tight deadlines. I look forward to discussing this further with you. I am submitting my resume to you in response to your advertisement for a Graphic Designer. I believe I have the skills that you are seeking and would like to be considered for this position. I have extensive layout and design experience and enjoy working on precise, detailed projects. I am highly organized and adept at meeting tight deadlines. I look forward to discussing this further with you. I am submitting my resume to you in response to your advertisement for a Graphic Designer. I believe I have the skills that you are seeking and would like to be considered for this position. I have extensive layout and design experience and enjoy working on precise, detailed projects. I am highly organized and adept at meeting tight deadlines. I look forward to discussing this further with you.</p>
  </div>

  <footer class="letter-footer">
    <div class="contact">Ph:555555 Cell:555555 Fax:555555 E-mail: dennis@larkfield-interiors-studio.com</div>
  </footer>
</section>

<section class="card card-front">
  <div class="person">
    <div class="name">Dennis Coyle</div>
    <div class="role">Project Manager</div>
  </div>
  <div class="brand">
    <span class="brand-mark"></span>
    <span class="brand-name">Larkfield<br>Interiors</span>
  </div>
  <div class="band"></div>
  <div class="contact">Ph:555555 Cell:555555 Fax:555555 E-mail: dennis@larkfield-interiors-studio.com</div>
</section>

<section class="card card-back">
  <div class="side"></div>
  <div class="person">
    <div class="name">Dennis Coyle</div>
    <div class="role">Project Manager</div>
  </div>
  <div class="brand">
    <span class="brand-mark"></span>
    <span class="brand-name">Larkfield<br>Interiors</span>
  </div>
  <div class="address">478 Oakmont Avenue N.W. Millbrook, WI 53021</div>
  <div class="contact">Ph:555555 Cell:555555 Fax:555555 E-mail: dennis@larkfield-interiors-studio.com</div>
  <div class="base"></div>
</section>

</body>
</html>
```